Brisket Glazing

Modern glazing company specializing in commercial fit outs, pool fencing, frameless showers and glass splash backs, im after a very young/modern logo, it doesnt have to be revelent to glazing and a classy "boss like" design for the card. thank you in advanced
Updates

im thinking carbon fiber back ground or something along that line with bright orange wording or something maybe, open to suggestions 

Industry/Entity Type

Fencing

Contact Information for Business Card

company name, name, phone and products

```html
<!DOCTYPE html>
<html lang="en">
<head>
<meta charset="utf-8">
<title>Brisket Glazing – Business Card Concepts</title>
<link rel="stylesheet" href="https://fonts.googleapis.com/css2?family=Arimo:wght@700&family=Roboto+Slab:wght@800&family=Roboto+Condensed:wght@700&family=PT+Sans:wght@400;700&display=swap">
<style>
  :root {
    --frame: #b9babc;
    --panel-light: #eeeff0;
    --panel-dark: #9c9ea1;
    --orange: #f7941d;
    --amber: #fbb417;
    --red: #e8332a;
    --deep-red: #c8262c;
    --ink: #1d1d1b;
    --white: #ffffff;
    --veil: rgba(255, 255, 255, 0.42);
    --ghost: rgba(235, 225, 225, 0.55);
  }
  * { margin: 0; padding: 0; box-sizing: border-box; }
  html, body { width: 948px; height: 1200px; overflow: hidden; }
  body { background: var(--frame); position: relative; }

  .presentation {
    position: absolute;
    left: 26px; top: 26px;
    width: 897px; height: 1146px;
    background: radial-gradient(ellipse 70% 60% at 50% 48%, var(--panel-light) 0%, #cfd0d2 55%, var(--panel-dark) 100%);
  }

  .card {
    position: absolute;
    width: 552px; height: 334px;
    overflow: hidden;
  }
  .card--shadowed { box-shadow: 14px 14px 16px rgba(0, 0, 0, 0.55); }
  .card--front-sun { left: 39px; top: 34px; }
  .card--front-corridor { left: 239px; top: 398px; }
  .card--back { left: 32px; top: 773px; }

  .card__art { position: absolute; inset: 0; }
  .card--front-sun .card__art {
    background:
      radial-gradient(ellipse 45% 55% at 38% 20%, var(--amber) 0%, rgba(251,180,23,0) 70%),
      linear-gradient(160deg, var(--orange) 0%, #f26b22 50%, var(--red) 100%);
  }
  .card--front-corridor .card__art {
    background:
      radial-gradient(ellipse 30% 45% at 50% 40%, #f9a23a 0%, rgba(249,162,58,0) 80%),
      linear-gradient(90deg, #c97b86 0%, var(--red) 25%, #f07a22 50%, var(--red) 75%, #c97b86 100%);
  }
  .card--back .card__art {
    background:
      radial-gradient(ellipse 55% 60% at 60% 40%, var(--orange) 0%, rgba(247,148,29,0) 80%),
      linear-gradient(135deg, #f06a36 0%, var(--red) 60%, var(--deep-red) 100%);
  }

  .company-name {
    position: absolute;
    font-family: "Arimo", Arial, sans-serif;
    font-weight: 700;
    font-size: 46px;
    line-height: 52px;
    color: var(--white);
    white-space: nowrap;
    letter-spacing: 1.5px;
    word-spacing: 14px;
  }
  .card--front-sun .company-name { left: 89px; top: 106px; }
  .card--front-corridor .company-name { left: 87px; top: 78px; }

  .contact-veil {
    position: absolute;
    left: 93px; top: 177px;
    width: 369px; height: 79px;
    background: var(--veil);
  }

  .contact {
    position: absolute;
    width: 552px;
    left: 0;
    text-align: center;
    color: var(--ink);
  }
  .card--front-sun .contact { top: 184px; left: 8px; }
  .card--front-corridor .contact { top: 177px; left: 0; }

  .contact__name {
    font-family: "Roboto Slab", Rockwell, Georgia, serif;
    font-weight: 800;
    font-size: 22px;
    letter-spacing: 1px;
    line-height: 26px;
  }
  .contact__phone {
    display: flex;
    justify-content: center;
    align-items: center;
    gap: 12px;
    margin-top: 4px;
  }
  .contact__label {
    font-family: "PT Sans", Arial, sans-serif;
    font-size: 21px;
  }
  .contact__dot { width: 10px; height: 10px; background: var(--ink); }
  .contact__number {
    font-family: "Roboto Condensed", "Arial Narrow", sans-serif;
    font-weight: 700;
    font-size: 31px;
    margin-left: 10px;
  }

  .ghost-word {
    position: absolute;
    font-family: "Arimo", Arial, sans-serif;
    font-weight: 700;
    line-height: normal;
    color: var(--ghost);
    white-space: nowrap;
    letter-spacing: 2px;
  }
  .ghost-word--top { left: 186px; top: -10px; font-size: 86px; }
  .ghost-word--bottom { left: 0; top: 220px; font-size: 88px; }

  .specialties {
    position: absolute;
    left: 30px; top: 56px;
    color: var(--ink);
    font-family: "PT Sans", Arial, sans-serif;
  }
  .specialties__title { font-weight: 700; font-size: 29px; line-height: 30px; }
  .specialties__list { list-style: none; margin: -4px 0 0 206px; }
  .specialties__item {
    display: flex; align-items: center; gap: 18px;
    font-size: 30px; line-height: 40.5px; letter-spacing: 0.3px;
  }
  .specialties__item::before {
    content: ""; width: 10px; height: 10px; background: var(--ink); flex: none;
  }
</style>
</head>
<body>
  <main class="presentation">

    <section class="card card--front-sun" aria-label="Business card front, sunburst version">
      <div class="card__art" role="img" aria-label="Orange and red perspective glass-tile background with a bright burst"></div>
      <h1 class="company-name">Brisket Glazing</h1>
      <div class="contact-veil"></div>
      <div class="contact">
        <p class="contact__name">DANE MORROW</p>
        <p class="contact__phone"><span class="contact__label">Tel</span><span class="contact__dot"></span><span class="contact__number">0491 570 156</span></p>
      </div>
    </section>

    <section class="card card--front-corridor card--shadowed" aria-label="Business card front, corridor version">
      <div class="card__art" role="img" aria-label="Orange corridor of glass tiles receding to a glowing centre"></div>
      <h2 class="company-name">Brisket Glazing</h2>
      <div class="contact">
        <p class="contact__name">DANE MORROW</p>
        <p class="contact__phone"><span class="contact__label">Tel</span><span class="contact__dot"></span><span class="contact__number">0491 570 156</span></p>
      </div>
    </section>

    <section class="card card--back card--shadowed" aria-label="Business card back">
      <div class="card__art" role="img" aria-label="Red-orange background of angled glass tiles"></div>
      <span class="ghost-word ghost-word--top">Brisket</span>
      <span class="ghost-word ghost-word--bottom">Glazing</span>
      <div class="specialties">
        <p class="specialties__title">Specialized in:</p>
        <ul class="specialties__list">
          <li class="specialties__item">commercial fit outs</li>
          <li class="specialties__item">pool fencing</li>
          <li class="specialties__item">frameless showers</li>
          <li class="specialties__item">glass splash backs</li>
        </ul>
      </div>
    </section>

  </main>
</body>
</html>
```